Vo Lunec - Business Cards & Stationnery
Think Ahead, Vo Lunec
Professional
Odile Fenwar Quintanel
48 rue des Glycines Doréales
75020 Paris
France
odile@volunec.com
www.volunec.com
The business cards have to be at the european standard ie 8,5 x 5,4 cm (seems to be 3.35'' x 2.13'')
Same for the stationnery ie A4 format, 21 x 29,7 cm (seems to be 8,27'' x 11.7'')
Please use the logo, name of the company and the base line: Think Ahead, Vo Lunec

```html
<!DOCTYPE html>
<html lang="fr">
<head>
<meta charset="utf-8">
<title>Vo Lunec – Business Card</title>
<link rel="stylesheet" href="https://fonts.googleapis.com/css2?family=PT+Sans:wght@400;700&display=swap">
<style>
  :root {
    --backdrop: #e9e6e2;
    --card: #ffffff;
    --purple: #5a2d86;
    --purple-deep: #3f1c63;
    --ink: #2b2b2b;
    --grey: #6f6f6f;
    --rule: #c9c9c9;
    --swoosh-dark: #1d1d1d;
  }
  html, body {
    margin: 0;
    width: 1200px;
    height: 780px;
    overflow: hidden;
    background: var(--backdrop);
    font-family: "PT Sans", Arial, sans-serif;
  }
  .business-card {
    position: absolute;
    left: 90px;
    top: 66px;
    width: 1020px;
    height: 648px;
    background: var(--card);
    border-radius: 26px;
    overflow: hidden;
    box-shadow: 0 6px 24px rgba(0,0,0,0.18);
  }
  .brand {
    position: absolute;
    left: 70px;
    top: 240px;
    width: 330px;
    text-align: center;
  }
  .brand-mark {
    display: inline-block;
    width: 34px;
    height: 34px;
    background: var(--purple);
    margin-bottom: 18px;
  }
  .brand-name {
    display: block;
    font-size: 54px;
    font-weight: 700;
    letter-spacing: 3px;
    color: var(--ink);
    line-height: 1;
  }
  .brand-tagline {
    display: block;
    margin-top: 10px;
    font-size: 17px;
    letter-spacing: 4px;
    color: var(--grey);
    text-transform: uppercase;
  }
  .divider {
    position: absolute;
    left: 440px;
    top: 40px;
    width: 2px;
    height: 420px;
    background: linear-gradient(to bottom, var(--rule), rgba(201,201,201,0));
  }
  .contact {
    position: absolute;
    left: 468px;
    top: 52px;
    color: var(--ink);
  }
  .contact-name {
    margin: 0;
    font-size: 30px;
    font-weight: 700;
    color: var(--purple);
  }
  .contact-address {
    margin: 92px 0 0;
    font-style: normal;
    font-size: 22px;
    line-height: 1.4;
    color: var(--grey);
  }
  .contact-lines {
    list-style: none;
    margin: 66px 0 0;
    padding: 0;
    font-size: 21px;
    color: var(--grey);
  }
  .contact-lines li {
    display: flex;
    align-items: center;
    gap: 12px;
    height: 31px;
  }
  .contact-lines svg { width: 18px; height: 18px; fill: var(--purple); }
  .swoosh {
    position: absolute;
    left: 0;
    bottom: 0;
    width: 1020px;
    height: 220px;
  }
</style>
</head>
<body>
  <div class="business-card">
    <div class="brand">
      <span class="brand-mark"></span>
      <span class="brand-name">VO LUNEC</span>
      <span class="brand-tagline">Think Ahead, Vo Lunec</span>
    </div>

    <div class="divider"></div>

    <div class="contact">
      <h1 class="contact-name">Odile Fenwar Quintanel</h1>
      <address class="contact-address">48 rue des Glycines Doréales<br>75020 Paris, France</address>
      <ul class="contact-lines">
        <li>
          <svg viewBox="0 0 18 18" aria-hidden="true"><rect x="4" y="1" width="10" height="16" rx="2"/><rect x="6" y="3" width="6" height="9" fill="#fff"/></svg>
          +33 (0)6 48 17 53 20
        </li>
        <li>
          <svg viewBox="0 0 18 18" aria-hidden="true"><rect x="1" y="3" width="16" height="12" rx="1"/><path d="M2 4 L9 10 L16 4" stroke="#fff" stroke-width="1.6" fill="none"/></svg>
          odile@volunec.com
        </li>
        <li>
          <svg viewBox="0 0 18 18" aria-hidden="true"><circle cx="9" cy="9" r="8"/><path d="M1 9 H17 M9 1 C5 5 5 13 9 17 M9 1 C13 5 13 13 9 17" stroke="#fff" stroke-width="1.2" fill="none"/></svg>
          www.volunec.com
        </li>
      </ul>
    </div>

    <svg class="swoosh" viewBox="0 0 1020 220" preserveAspectRatio="none" aria-hidden="true">
      <defs>
        <linearGradient id="band-purple" x1="0" y1="0" x2="1" y2="0">
          <stop offset="0" stop-color="var(--purple-deep)"/>
          <stop offset="0.5" stop-color="var(--purple)"/>
          <stop offset="1" stop-color="#7a4aa6"/>
        </linearGradient>
      </defs>
      <path d="M0 92 C300 135 700 120 1020 40 L1020 52 C700 132 300 148 0 108 Z" fill="var(--swoosh-dark)"/>
      <path d="M0 124 C320 165 720 140 1020 58 L1020 220 L0 220 Z" fill="url(#band-purple)"/>
      <path d="M0 124 C320 165 720 140 1020 58" stroke="#ffffff" stroke-width="4" fill="none"/>
    </svg>
  </div>
</body>
</html>
```